Business Card Design

I am an child sleep consultant. I would like the picture to be the background of the card and for my logo to be in the upper right hand corner. Other than that, the design is yours!!

Business

Marta Kovel
Red Fern Slumber
Certified Child Sleep Consultant
(555) 286-9153
redfernslumber.com

```html
<!DOCTYPE html>
<html lang="en">
<head>
<meta charset="utf-8">
<title>Marta Kovel – Red Fern Slumber</title>
<link rel="stylesheet" href="https://fonts.googleapis.com/css2?family=Tinos&display=swap">
<style>
  :root {
    --ink-black: #000000;
    --band-red: #c8232c;
    --text-white: #ffffff;
    --sepia-light: #f6b860;
    --sepia-mid: #d9782a;
    --sepia-warm: #b85a1c;
    --sepia-deep: #5a200a;
    --brand-glow: #ffd23c;
  }
  html, body {
    margin: 0;
    padding: 0;
    overflow: hidden;
    background: var(--ink-black);
  }
  .card {
    position: relative;
    width: 1200px;
    height: 686px;
    background: var(--ink-black);
    overflow: hidden;
    font-family: "Tinos", "Times New Roman", serif;
    color: var(--text-white);
  }
  .hero {
    position: absolute;
    left: 0;
    top: 0;
    width: 1200px;
    height: 448px;
  }
  .brand-name {
    position: absolute;
    left: 1030px;
    top: 30px;
    width: 150px;
    text-align: center;
    font-size: 26px;
    line-height: 1.15;
    color: var(--brand-glow);
    margin: 0;
  }
  .social {
    position: absolute;
    left: 32px;
    top: 357px;
    display: flex;
    flex-direction: column;
    gap: 16px;
  }
  .social-dot {
    width: 30px;
    height: 30px;
    border-radius: 50%;
    background: var(--text-white);
  }
  .contact-band {
    position: absolute;
    left: 0;
    top: 448px;
    width: 1200px;
    height: 238px;
    background: var(--band-red);
  }
  .icon {
    position: absolute;
    left: 34px;
    width: 26px;
    height: 26px;
    fill: var(--text-white);
  }
  .icon-pin { top: 453px; }
  .icon-phone { top: 519px; }
  .icon-mail { top: 583px; }
  .icon-web { top: 646px; }
  .identity {
    position: absolute;
    left: 98px;
    top: 448px;
    margin: 0;
    font-size: 30px;
    line-height: 39px;
  }
  .website {
    position: absolute;
    left: 98px;
    top: 636px;
    margin: 0;
    font-size: 36px;
    line-height: 44px;
  }
</style>
</head>
<body>
<div class="card">
  <svg class="hero" viewBox="0 0 1200 448" role="img" aria-label="Sepia-toned portrait of a baby over riveted wooden planks with a sunset sky">
    <defs>
      <radialGradient id="sepiaGlow" cx="0.5" cy="0.35" r="0.75">
        <stop offset="0" stop-color="var(--sepia-light)"/>
        <stop offset="0.45" stop-color="var(--sepia-mid)"/>
        <stop offset="0.8" stop-color="var(--sepia-warm)"/>
        <stop offset="1" stop-color="var(--sepia-deep)"/>
      </radialGradient>
    </defs>
    <path d="M306 0 Q298 250 349 448 L1200 448 L1200 0 Z" fill="url(#sepiaGlow)"/>
  </svg>

  <p class="brand-name">Red Fern Slumber</p>

  <div class="social" aria-label="Social links">
    <div class="social-dot"></div>
    <div class="social-dot"></div>
  </div>

  <div class="contact-band"></div>

  <svg class="icon icon-pin" viewBox="0 0 24 24" aria-hidden="true">
    <path d="M12 2a7 7 0 0 0-7 7c0 5 7 13 7 13s7-8 7-13a7 7 0 0 0-7-7zm0 9.5A2.5 2.5 0 1 1 12 6.5a2.5 2.5 0 0 1 0 5z"/>
  </svg>
  <svg class="icon icon-phone" viewBox="0 0 24 24" aria-hidden="true">
    <path d="M6.6 10.8a15.1 15.1 0 0 0 6.6 6.6l2.2-2.2a1 1 0 0 1 1-.25 11.4 11.4 0 0 0 3.6.57 1 1 0 0 1 1 1V20a1 1 0 0 1-1 1A17 17 0 0 1 3 4a1 1 0 0 1 1-1h3.5a1 1 0 0 1 1 1c0 1.25.2 2.46.57 3.6a1 1 0 0 1-.25 1z"/>
  </svg>
  <svg class="icon icon-mail" viewBox="0 0 24 24" aria-hidden="true">
    <path d="M2 5h20v14H2z M3.5 6.5v11h17v-11l-8.5 6.5z M4.8 6.5 12 11.8l7.2-5.3z" fill-rule="evenodd"/>
  </svg>
  <svg class="icon icon-web" viewBox="0 0 24 24" aria-hidden="true">
    <path d="M12 2a10 10 0 1 0 0 20 10 10 0 0 0 0-20zm0 1.8c1 1.2 1.9 3.2 2.2 5.4H9.8C10.1 7 11 5 12 3.8zM9.6 10.8h4.8a15 15 0 0 1 0 2.4H9.6a15 15 0 0 1 0-2.4zm.2 4h4.4C13.9 17 13 19 12 20.2 11 19 10.1 17 9.8 14.8zM3.9 10.8h4.1a17 17 0 0 0 0 2.4H3.9a8 8 0 0 1 0-2.4zm12.1 0h4.1a8 8 0 0 1 0 2.4H16a17 17 0 0 0 0-2.4zM4.5 9.2a8.3 8.3 0 0 1 4.3-4.5 11 11 0 0 0-1.4 4.5zm10.7-4.5a8.3 8.3 0 0 1 4.3 4.5h-2.9a11 11 0 0 0-1.4-4.5zM4.5 14.8h2.9a11 11 0 0 0 1.4 4.5 8.3 8.3 0 0 1-4.3-4.5zm12.1 0h2.9a8.3 8.3 0 0 1-4.3 4.5 11 11 0 0 0 1.4-4.5z"/>
  </svg>

  <p class="identity">Marta Kovel Red Fern Slumber Certified Child Sleep Consultant<br>(555) 286-9153</p>
  <p class="website">redfernslumber.com</p>
</div>
</body>
</html>
```